We are growing our coaching practice and need some help creating collateral

Our organisation is building a coaching practice. It's going well and we want to take it to the next level. To date, we've done our own basic marketing material (attached), but now we want to create something more substantial that captures our approach and gives us confidence and pride when talking to customers. Things to note - we aren't looking for logo design, that's a separate branding discussion in our organisation. We are looking for someone to take our existing content and make it look good - this might be in the form of a flyer or PPT slide deck for example.
The format we are looking for is the offering title - in this case, 'Coaching', a brief description, and then some further detail.
Target Market(s)
Corporate, Healthcare, IT
Colors
Designer to choose colors to be used in the design.
Look and feel
Each slider illustrates characteristics of the customer's brand and the style your logo design should communicate.

```html
<!DOCTYPE html>
<html lang="en">
<head>
<meta charset="utf-8">
<title>Tandem Executive Coaching – Flyer</title>
<link href="https://fonts.googleapis.com/css2?family=Open+Sans:wght@400;600;700&family=Oswald:wght@500;600&display=swap" rel="stylesheet">
<style>
:root{
  --bg:#c49a6c;
  --paper:#ffffff;
  --paper-soft:#f3f2f4;
  --ink:#3a3a3c;
  --body:#444446;
  --orange:#f39322;
  --orange-deep:#e8633a;
  --yellow:#f6d21e;
  --dark:#3d3b3d;
  --photo-b:#d9cfc4;
}
*{margin:0;padding:0;box-sizing:border-box}
html,body{width:1200px;height:831px;overflow:hidden;background:var(--bg)}
body{position:relative;font-family:"Open Sans",Arial,sans-serif;color:var(--body)}
.page{position:absolute;top:78px;width:548px;height:707px;background:var(--paper);overflow:hidden;box-shadow:4px 6px 10px rgba(0,0,0,.35)}
.page--back{left:40px}
.page--front{left:614px;background:var(--paper-soft)}
.abs{position:absolute}
.display{font-family:"Oswald",Arial,sans-serif;font-weight:600;letter-spacing:.2px}

/* back */
.coach-title{left:38px;top:34px;font-size:27px;font-weight:700;line-height:31px;color:var(--ink)}
.coach-bio{left:38px;top:110px;width:246px;font-size:7.6px;line-height:12.4px;text-align:justify}
.coach-bio p+p{margin-top:6px}
.quals-title{left:322px;top:56px;font-size:13px;font-weight:600;line-height:16px;color:var(--orange)}
.quals{left:322px;top:112px;width:214px;list-style:none;font-size:7.4px;font-weight:600;color:var(--ink)}
.quals li{position:relative;padding-left:16px;line-height:10.5px;margin-bottom:5.5px}
.quals svg{position:absolute;left:0;top:1px}
.coach-note{left:38px;top:268px;width:430px;font-size:12px;font-weight:600;line-height:18px;color:var(--orange-deep)}
.infographic{left:38px;top:326px;width:300px;height:90px;background:linear-gradient(180deg,#f4f5f6,#e3e6e9);border-radius:3px}
.back-band{left:0;top:431px;width:548px;height:64px;background:var(--dark)}
.back-band h2{position:absolute;left:33px;top:11px;font-size:32px;line-height:42px;color:var(--orange)}
.back-photo{left:0;top:495px;width:548px;height:165px;background:linear-gradient(135deg,#7d8791,#c9c2b7 60%,#e8e2d8)}
.back-foot{left:0;top:660px;width:548px;height:47px;background:var(--dark);color:#fff;font-size:13.4px;font-weight:700;padding:14px 0 0 24px;white-space:nowrap}
.seal{left:396px;top:364px;width:120px;height:120px;border-radius:50%;background:#fff;border:5px solid #b9b9bb}

/* front */
.front-art{left:0;top:0}
.brand{left:24px;top:32px;font-size:22px;font-weight:400;color:var(--ink);letter-spacing:1px}
.site{left:258px;top:30px;font-size:19px;font-weight:700;color:#111}
.badge{left:367px;top:230px;width:124px;height:124px;border-radius:50%;background:var(--dark);border:4px solid var(--yellow);color:#fff;font-size:21px;line-height:28px;display:flex;align-items:center;justify-content:center;text-align:center}
.front-title{left:25px;top:376px;font-size:37px;line-height:46px;color:var(--ink);white-space:nowrap}
.lead{left:25px;top:434px;font-size:11px;color:#222}
.intro{left:25px;top:451px;width:264px;font-size:7.5px;line-height:11.6px;text-align:justify;color:var(--body)}
.intro p+p{margin-top:4px}
.packages{left:322px;top:452px;width:210px}
.packages h3{font-size:15px;font-weight:700;color:var(--orange-deep);line-height:20px}
.packages .sub{font-size:9.6px;font-weight:600;color:var(--ink);line-height:13px;margin-top:3px}
.packages .price{font-size:11px;font-weight:600;color:var(--orange-deep);line-height:15px;margin-top:8px}
.packages .fine{font-size:7.3px;line-height:11.4px;color:#555;margin-top:8px}
.contact-tab{left:310px;top:610px}
.contact-tab span{position:absolute;left:16px;top:7px;font-size:15px;color:#fff;white-space:nowrap}
.contact-tab b{font-weight:700}
.front-foot{left:0;top:642px;width:548px;height:66px;background:var(--orange-deep)}
.front-foot .offer{position:absolute;left:27px;top:9px;width:265px;font-size:7.6px;font-weight:700;line-height:11.4px;color:#fff;text-transform:uppercase}
.front-foot .call{position:absolute;left:320px;top:6px;font-size:20px;font-weight:700;color:#fff}
.front-foot .mail{position:absolute;left:320px;top:35px;font-size:9.6px;font-weight:600;letter-spacing:.3px;color:#fff}
</style>
</head>
<body>

<section class="page page--back">
  <svg class="abs" style="left:0;top:0" width="548" height="60" viewBox="0 0 548 60">
    <path d="M292 0H548V38C470 60 380 30 292 0Z" fill="var(--orange)"/>
    <path d="M430 46C480 50 520 44 548 38V42C520 50 480 54 430 46Z" fill="#6b6b6e"/>
  </svg>

  <h1 class="abs coach-title">Meet one of our<br>Coaches</h1>

  <div class="abs coach-bio">
    <p>Dan Morrow leads the Executive Coaching practice for Tandem across Australia and New Zealand.</p>
    <p>He has worked at senior levels in the State Public Service, the Federal Public Service and in the private sector. His continuing focus over the past 20 years has been on organisational and people development. As a Masters-qualified and highly experienced executive coach, Dan's passion lies in unlocking human potential. He has coached doctors, nurses, allied health clinicians, statisticians, scientists, educators, IT professionals, Senior managers and Executives in the federal service (Level 1 – Senior Executive), State Government (Executive bands) and private sector.</p>
  </div>

  <h2 class="abs quals-title">Qualifications,<br>Accreditations,<br>Memberships</h2>
  <ul class="abs quals">
    <li><svg width="10" height="10" viewBox="0 0 10 10"><rect x=".5" y=".5" width="9" height="9" fill="none" stroke="var(--orange)"/><path d="M2 5l2 2 4-5" fill="none" stroke="#2b7bb9" stroke-width="1.4"/></svg>Master of Science in Coaching Psychology</li>
    <li><svg width="10" height="10" viewBox="0 0 10 10"><rect x=".5" y=".5" width="9" height="9" fill="none" stroke="var(--orange)"/><path d="M2 5l2 2 4-5" fill="none" stroke="#2b7bb9" stroke-width="1.4"/></svg>Graduate Certificate in Management</li>
    <li><svg width="10" height="10" viewBox="0 0 10 10"><rect x=".5" y=".5" width="9" height="9" fill="none" stroke="var(--orange)"/><path d="M2 5l2 2 4-5" fill="none" stroke="#2b7bb9" stroke-width="1.4"/></svg>Certificate IV in Workplace Assessment &amp; Training</li>
    <li><svg width="10" height="10" viewBox="0 0 10 10"><rect x=".5" y=".5" width="9" height="9" fill="none" stroke="var(--orange)"/><path d="M2 5l2 2 4-5" fill="none" stroke="#2b7bb9" stroke-width="1.4"/></svg>LPI/GPI Accreditation, Human Dynamics Group</li>
    <li><svg width="10" height="10" viewBox="0 0 10 10"><rect x=".5" y=".5" width="9" height="9" fill="none" stroke="var(--orange)"/><path d="M2 5l2 2 4-5" fill="none" stroke="#2b7bb9" stroke-width="1.4"/></svg>Type Profile Accreditation</li>
    <li><svg width="10" height="10" viewBox="0 0 10 10"><rect x=".5" y=".5" width="9" height="9" fill="none" stroke="var(--orange)"/><path d="M2 5l2 2 4-5" fill="none" stroke="#2b7bb9" stroke-width="1.4"/></svg>Member, Global Coaching Guild (GCG)</li>
    <li><svg width="10" height="10" viewBox="0 0 10 10"><rect x=".5" y=".5" width="9" height="9" fill="none" stroke="var(--orange)"/><path d="M2 5l2 2 4-5" fill="none" stroke="#2b7bb9" stroke-width="1.4"/></svg>Member, Harbour University Coaching &amp; Mentoring Alumni Association</li>
  </ul>

  <p class="abs coach-note">When Dan is not coaching, he is facilitating workshops and consulting to enable teams and organisations to make effective transformations.</p>

  <div class="abs infographic" role="img" aria-label="Coaching infographic: motivation, coach, potential, development, skill, support, knowledge and advice icons"></div>

  <div class="abs back-band"><h2 class="display">Tandem Executive Coaching</h2></div>
  <div class="abs back-photo" role="img" aria-label="Photo of hands working at a laptop with printed notes on a desk"></div>
  <div class="abs back-foot">For details on other Tandem services please visit www.tandemcoaching.com</div>
  <div class="abs seal"></div>
</section>

<section class="page page--front">
  <svg class="abs front-art" width="548" height="380" viewBox="0 0 548 380">
    <defs>
      <clipPath id="photoClip"><path d="M0 0H440C500 60 510 170 470 250C420 320 330 340 220 342C130 344 60 334 0 318Z"/></clipPath>
      <linearGradient id="photoTone" x1="0" y1="0" x2="1" y2="1">
        <stop offset="0" stop-color="#eef0f2"/><stop offset=".45" stop-color="var(--photo-b)"/><stop offset="1" stop-color="#6f6a66"/>
      </linearGradient>
    </defs>
    <path d="M0 318C60 334 130 344 220 342C330 340 420 320 470 250C500 200 505 150 494 112C520 170 520 250 480 300C420 360 320 372 220 372C130 372 60 362 0 348Z" fill="var(--orange)"/>
    <rect width="548" height="360" fill="url(#photoTone)" clip-path="url(#photoClip)" role="img" aria-label="Photo of a seminar audience listening to a speaker"/>
    <rect width="548" height="70" fill="var(--paper-soft)" opacity=".8" clip-path="url(#photoClip)"/>
    <path d="M440 0H470C520 70 530 170 494 250C505 170 490 70 440 0Z" fill="var(--orange)"/>
    <path d="M478 0H500C540 60 548 130 530 190C535 120 520 60 478 0Z" fill="var(--yellow)"/>
  </svg>

  <div class="abs brand">tandem coaching</div>
  <div class="abs site">tandemcoaching.com</div>
  <div class="abs badge display">7 Hourly<br>Sessions</div>

  <h1 class="abs front-title display">Tandem Executive Coaching</h1>
  <p class="abs lead">We believe great coaching is a bridge:</p>
  <div class="abs intro">
    <p>one that enables you to see more clearly and cross the unexpected chasms; one that supports and challenges your thinking and actions to progress your significant goals.</p>
    <p>We build a creative and confidential partnership with you, one that is grounded in the science of leadership, change and coaching psychology so that practical results are an expectation and not left to chance.</p>
    <p>Our coaches are highly attuned to the human systems within which you work and live, since understanding those interconnected forces is vital to unlock movement. We build on your existing strengths and seek sustainable shifts, ones that create ripple effects of positive change.</p>
    <p>Leaders everywhere face unprecedented change, pressure, ambiguity, culture and accountability dilemmas. And yet every leader also has a different story, different terrain to navigate and different aspirations. This is where executive coaching with Tandem can create extraordinary results.</p>
  </div>

  <div class="abs packages">
    <h3>OUR COACHING PACKAGES</h3>
    <p class="sub">typically consist of blocks of 7 Hourly Sessions, conducted fortnightly (with flexibility to customise).</p>
    <p class="price">For Level 2 leaders, the investment in a block of 7 sessions is $3400 + GST.</p>
    <p class="fine">This includes significant preparation and conceptualisation time before and after sessions by your coach to ensure you achieve maximum value.</p>
  </div>

  <svg class="abs contact-tab" width="196" height="33" viewBox="0 0 196 33">
    <path d="M10 0H186L196 33H0Z" fill="var(--dark)"/>
  </svg>
  <div class="abs contact-tab"><span>Contact <b>Dan Morrow</b></span></div>

  <div class="abs front-foot">
    <p class="offer">Why not explore the possibilities executive coaching offers through a no obligation initial session, ensuring the approach and the coach is a good fit for you?</p>
    <p class="call">Call: 0400 123 456</p>
    <p class="mail">dan.morrow@tandemcoaching.com</p>
  </div>
</section>

</body>
</html>
```